International business needs business cards

Our company, DOR Ventures Inc. is in the business of supplying a range construction products with particular emphasis on CEMENT. We have developed our own brand - BRUNVALE MATERIALS - with which to infiltrate the market. We are launching our brand of cement (BRUNVALE Type IS Cement) into the Caribbean which is unlike anything this market has ever seen. A monopoly has existed here for the past 60-odd years and the market has now opened to allow the importation of other brands and consumers are anxious and ready for change/improvement. We are very excited to be launching and want to make a great first impression. We will be conducting workshops and seminars (from government level to the hardware store owners) and we want our business card to give us the strong, confident introduction that we need.

Target Market(s)

construction; builders; engineers; home owners

Industry/Entity Type

Construction

Contact Information for Business Card

Marisol Penwick
CEO
cell # 1 555 4817730
Ground floor,Lantern Plaza Suite 2483
George Town,Grand Cayman
Cayman Islands,KY1-2250
EMAIL: m.penwick@dorventuresinc.example
web site dorventuresinc.example

COMPANY: skype info dor.ventures.example

second card
Tamsin Rowe-Penwick
CFO
CELL# 1 555 604 3917
George Town,Grand Cayman
Cayman Islands,KY1-2250
EMAIL: t.rowepenwick@dorventuresinc.example
website dorventuresinc.example

Requirements
Must have
• Business cards must display BOTH logos - DOR is the company and BRUNVALE is the brand.

```html
<!DOCTYPE html>
<html lang="en">
<head>
<meta charset="utf-8">
<title>DOR Ventures Inc. — Business Card</title>
<link rel="stylesheet" href="https://fonts.googleapis.com/css2?family=Open+Sans:wght@400;600;700&display=swap">
<style>
  :root {
    --stage: #2b2b2b;
    --card: #0f0f0f;
    --card-edge: #1c1c1c;
    --brand-red: #8a1a1c;
    --text: #f2f2f2;
    --text-soft: #d4d4d4;
    --badge: #6a6a6a;
  }
  * { box-sizing: border-box; margin: 0; padding: 0; }
  html, body {
    width: 1200px; height: 900px; overflow: hidden;
    background: var(--stage);
    font-family: "Open Sans", Arial, sans-serif;
    color: var(--text);
  }
  .stage {
    position: relative; width: 1200px; height: 900px;
    display: flex; align-items: center; justify-content: center; gap: 48px;
  }
  .card {
    position: relative; width: 525px; height: 300px;
    background: var(--card);
    border: 1px solid var(--card-edge);
    border-radius: 18px;
  }
  /* Front: contact side */
  .card-front .mark-square {
    position: absolute; left: 62px; top: 72px;
    width: 150px; height: 150px; background: var(--brand-red);
  }
  .card-front .mark-name {
    position: absolute; left: 62px; top: 234px; width: 150px;
    font-size: 13px; font-weight: 700; text-align: center; color: var(--text);
  }
  .contact {
    position: absolute; left: 262px; top: 44px;
  }
  .contact .person { font-size: 17px; font-weight: 700; line-height: 1.2; }
  .contact .role { font-size: 12px; color: var(--text-soft); margin-bottom: 10px; }
  .contact .address { font-size: 12.5px; line-height: 1.5; color: var(--text-soft); margin-bottom: 6px; }
  .contact ul { list-style: none; }
  .contact li {
    display: flex; align-items: center; gap: 9px;
    font-size: 12.5px; line-height: 1.6; color: var(--text-soft);
  }
  .contact li svg { width: 10px; height: 10px; fill: var(--text); flex: none; }
  .brand-badge {
    position: absolute; left: 262px; top: 226px;
    display: flex; align-items: center; gap: 8px;
  }
  .brand-badge .dot { width: 30px; height: 30px; border-radius: 50%; background: var(--badge); }
  .brand-badge .name { font-size: 12px; font-weight: 700; color: var(--text-soft); letter-spacing: .5px; }
  /* Back: logo side */
  .card-back { display: flex; align-items: center; justify-content: center; gap: 14px; }
  .card-back .mark-square { width: 88px; height: 88px; background: var(--brand-red); }
  .card-back .mark-name { font-size: 30px; font-weight: 700; color: var(--text); line-height: 1.1; }
</style>
</head>
<body>
<main class="stage">
  <section class="card card-front" aria-label="Business card front">
    <div class="mark-square"></div>
    <div class="mark-name">DOR Ventures Inc.</div>
    <div class="contact">
      <p class="person">Marisol Penwick</p>
      <p class="role">CEO</p>
      <p class="address">Ground floor, Lantern Plaza Suite 2483<br>George Town, Grand Cayman<br>Cayman Islands, KY1-2250</p>
      <ul>
        <li><svg viewBox="0 0 10 10"><path d="M2 0.5 L3.6 2.6 L2.8 3.7 Q4 6 6.3 7.2 L7.4 6.4 L9.5 8 L8.4 9.5 Q3.5 9 0.5 1.6 Z"/></svg>1 555 4817730</li>
        <li><svg viewBox="0 0 10 10"><path d="M0.5 2 H9.5 V8.5 H0.5 Z M1.2 2.6 L5 5.6 L8.8 2.6" stroke="#0f0f0f" stroke-width=".8"/></svg>m.penwick@dorventuresinc.example</li>
        <li><svg viewBox="0 0 10 10"><circle cx="5" cy="5" r="4.5"/></svg>www.dorventuresinc.example</li>
      </ul>
    </div>
    <div class="brand-badge">
      <span class="dot"></span>
      <span class="name">BRUNVALE</span>
    </div>
  </section>
  <section class="card card-back" aria-label="Business card back">
    <div class="mark-square"></div>
    <div class="mark-name">DOR Ventures Inc.</div>
  </section>
</main>
</body>
</html>
```